Book cover Design for her new book called 'Walking a path lit by courage and grace'

My name is Velarosha, I am the founder of The Quiet Lantern.
http://velarosha-wren.shopnestle.example/
My book is an inspirational story of love and triumphing from adversity. After 40 years of surviving a life full of sexual abuse, physical and mental abuse and living with the effects of poor self-esteem and post traumatic stress disorder, this book is a guide to help others navigate away from negative emotions and help them find their own light in life. With the techniques developed and described in the book The Quiet Lantern's mission is to empower people with the journey to their own hearts and create warmth, love and inspiration.
The colours in the website represent the softness that I love and I prefer flowers. The colour also can be soft as well as vibrant and feminine. The final design should represent healing, love, inspiration and passion.

Target Market(s)

Women over the age of 25 -80
Teenagers suffering from depression
Men and women suffering from poor self esteem
Woman who have poor self confidence.

Requirements
Should not have
• Should not be dark in colour or imagery.

```html
<!DOCTYPE html>
<html lang="en">
<head>
<meta charset="utf-8">
<title>Walking a path lit by courage and grace — Book Cover</title>
<link href="https://fonts.googleapis.com/css2?family=Arimo:wght@400;500&family=Dancing+Script:wght@500&display=swap" rel="stylesheet">
<style>
  :root {
    --page-bg: #ffffff;
    --sky-top: #1f4f9e;
    --sky-mid: #0d46a0;
    --sky-low: #2f6fc0;
    --grass: #3f9a2a;
    --grass-light: #6cbc3e;
    --ink-light: #ffffff;
    --rule: rgba(255,255,255,0.85);
  }
  * { margin: 0; padding: 0; box-sizing: border-box; }
  html, body {
    width: 1200px;
    height: 900px;
    overflow: hidden;
    background: var(--page-bg);
  }
  .canvas {
    position: relative;
    width: 1200px;
    height: 900px;
  }
  .book-cover {
    position: absolute;
    left: 282px;
    top: 0;
    width: 636px;
    height: 900px;
    overflow: hidden;
    color: var(--ink-light);
  }
  .cover-photo {
    position: absolute;
    inset: 0;
    background:
      linear-gradient(to bottom, transparent 0, transparent 836px, var(--grass-light) 838px, var(--grass) 900px),
      linear-gradient(160deg, var(--sky-top) 0%, var(--sky-mid) 45%, var(--sky-low) 92%);
  }
  .author-line {
    position: absolute;
    top: 40px;
    left: 0;
    right: 0;
    display: flex;
    align-items: center;
    gap: 14px;
  }
  .author-line .rule {
    flex: 1;
    height: 1px;
    background: var(--rule);
  }
  .author-name {
    font-family: "Arimo", Arial, sans-serif;
    font-weight: 500;
    font-size: 22px;
    letter-spacing: 4px;
  }
  .title {
    position: absolute;
    top: 128px;
    left: 66px;
    right: 20px;
  }
  .title-lead {
    font-family: "Arimo", Arial, sans-serif;
    font-weight: 400;
    font-size: 64px;
    line-height: 64px;
    letter-spacing: 0.5px;
  }
  .title-sub {
    font-family: "Arimo", Arial, sans-serif;
    font-weight: 400;
    font-size: 37px;
    line-height: 38px;
    margin-left: 12px;
  }
  .title-script {
    font-family: "Dancing Script", cursive;
    font-weight: 500;
    font-size: 150px;
    line-height: 130px;
    transform: rotate(-8deg);
    transform-origin: left center;
    white-space: nowrap;
  }
  .title-script.first { margin-top: 24px; margin-left: 0; }
  .title-script.second { margin-left: 30px; margin-top: 8px; }
</style>
</head>
<body>
<main class="canvas">
  <section class="book-cover">
    <div class="cover-photo" role="img" aria-label="Photograph of a woman leaping across a green meadow under a clear blue sky, trailing a long flowing lime-green scarf"></div>
    <div class="author-line">
      <span class="rule"></span>
      <span class="author-name">VELAROSHA</span>
      <span class="rule"></span>
    </div>
    <h1 class="title">
      <div class="title-lead">WALKING</div>
      <div class="title-sub">A PATH LIT BY</div>
      <div class="title-script first">courage</div>
      <div class="title-script second">and grace</div>
    </h1>
  </section>
</main>
</body>
</html>
```